Business Card Design-Meridel Consulting. Computer Consultant. Meridel Personnel-Specialising IT.

I have 3 businesses-2 directed at the computer industry1) Meridel Personnel. Specialising in computer staff selection and placement2) Meridel Consulting. Specialising in ERP Software selection & implementation.1) Meridel BRQ.

Business

Three Different Cards:1) Meridel Personnel2) Meridel Consulting3) Meridel-BRQ

```html
<!DOCTYPE html>
<html lang="en">
<head>
<meta charset="utf-8">
<title>Meridel Business Cards</title>
<link rel="stylesheet" href="https://fonts.googleapis.com/css2?family=Questrial&display=swap">
<style>
  :root {
    --backdrop: #2c2c2c;
    --card: #ffffff;
    --slate: #4f6f79;
    --slate-back: #557680;
    --ink: #3d4f57;
    --accent: #1aa7d9;
    --white: #ffffff;
  }
  * { box-sizing: border-box; margin: 0; padding: 0; }
  html, body {
    width: 1200px; height: 750px; overflow: hidden;
    background: var(--backdrop);
    font-family: "Questrial", "Century Gothic", sans-serif;
  }
  .sheet { position: relative; width: 1200px; height: 750px; }
  .card {
    position: absolute;
    width: 496px; height: 284px;
    background: var(--card);
    overflow: hidden;
  }
  .card--personnel { left: 89px; top: 81px; }
  .card--back { left: 619px; top: 81px; background: var(--slate-back); }
  .card--consulting { left: 89px; top: 400px; height: 281px; }
  .card--brq { left: 619px; top: 400px; height: 281px; }

  .holder { position: absolute; left: 36px; top: 55px; }
  .holder__name { font-size: 12.5px; color: var(--ink); letter-spacing: .3px; }
  .holder__title { font-size: 12px; color: var(--accent); margin-top: 2px; }

  .address {
    position: absolute; left: 35px; top: 136px;
    font-size: 12.5px; line-height: 15px; color: var(--ink);
  }
  .contact {
    position: absolute; left: 35px; top: 183px;
    list-style: none; font-size: 14px; line-height: 16px; color: var(--ink);
  }
  .contact li { display: flex; align-items: center; gap: 4px; }
  .contact svg { width: 10px; height: 10px; fill: var(--ink); }

  .rule {
    position: absolute; left: 0; top: 240px;
    width: 311px; height: 3px; background: var(--accent);
  }
  .web {
    position: absolute; left: 319px; top: 232px;
    font-size: 14px; color: var(--ink); letter-spacing: .3px;
  }
  .card--brq .rule { width: 312px; }

  .brand {
    position: absolute; right: 38px; top: 92px;
    width: 230px; text-align: right;
    font-size: 30px; line-height: 30px; color: var(--slate);
  }
  .card--brq .brand { top: 104px; }

  .brand--back {
    position: absolute; left: 0; right: 0; top: 112px;
    text-align: center; font-size: 62px; color: var(--white);
  }
</style>
</head>
<body>
<div class="sheet">

  <section class="card card--personnel">
    <div class="holder">
      <p class="holder__name">EMPLOYEE NAME</p>
      <p class="holder__title">Title</p>
    </div>
    <p class="brand">Meridel Personnel</p>
    <p class="address">482 Harbor Row Suite 210,<br>Oregon USA 97035</p>
    <ul class="contact">
      <li><svg viewBox="0 0 10 10"><rect x="0" y="0" width="10" height="10" rx="1.5"/><path d="M3 2.2c-.5.4-.7 1.2-.2 2.3.6 1.4 1.8 2.7 3.1 3.3.8.3 1.4.1 1.7-.3l-1.1-1.1-.8.5c-.7-.4-1.3-1-1.7-1.7l.5-.8z" fill="#fff"/></svg>800.555.0142</li>
      <li><svg viewBox="0 0 10 10"><rect x="2.5" y="0.5" width="5" height="3"/><rect x="0" y="3.5" width="10" height="4" rx="1"/><rect x="2.5" y="6.5" width="5" height="3"/></svg>800.555.0199</li>
      <li><svg viewBox="0 0 10 10"><rect x="0" y="2" width="10" height="6.5"/><path d="M0.5 2.5 5 6 9.5 2.5" stroke="#fff" fill="none"/></svg>hello@meridelgroup.net</li>
    </ul>
    <div class="rule"></div>
    <p class="web">www.meridelgroup.net</p>
  </section>

  <section class="card card--back">
    <p class="brand--back">Meridel</p>
  </section>

  <section class="card card--consulting">
    <div class="holder">
      <p class="holder__name">EMPLOYEE NAME</p>
      <p class="holder__title">Title</p>
    </div>
    <p class="brand">Meridel Consulting</p>
    <p class="address">482 Harbor Row Suite 210,<br>Oregon USA 97035</p>
    <ul class="contact">
      <li><svg viewBox="0 0 10 10"><rect x="0" y="0" width="10" height="10" rx="1.5"/><path d="M3 2.2c-.5.4-.7 1.2-.2 2.3.6 1.4 1.8 2.7 3.1 3.3.8.3 1.4.1 1.7-.3l-1.1-1.1-.8.5c-.7-.4-1.3-1-1.7-1.7l.5-.8z" fill="#fff"/></svg>800.555.0142</li>
      <li><svg viewBox="0 0 10 10"><rect x="2.5" y="0.5" width="5" height="3"/><rect x="0" y="3.5" width="10" height="4" rx="1"/><rect x="2.5" y="6.5" width="5" height="3"/></svg>800.555.0199</li>
      <li><svg viewBox="0 0 10 10"><rect x="0" y="2" width="10" height="6.5"/><path d="M0.5 2.5 5 6 9.5 2.5" stroke="#fff" fill="none"/></svg>hello@meridelgroup.net</li>
    </ul>
    <div class="rule"></div>
    <p class="web">www.meridelgroup.net</p>
  </section>

  <section class="card card--brq">
    <div class="holder">
      <p class="holder__name">EMPLOYEE NAME</p>
      <p class="holder__title">Title</p>
    </div>
    <p class="brand">Meridel BRQ</p>
    <p class="address">482 Harbor Row Suite 210,<br>Oregon USA 97035</p>
    <ul class="contact">
      <li><svg viewBox="0 0 10 10"><rect x="0" y="0" width="10" height="10" rx="1.5"/><path d="M3 2.2c-.5.4-.7 1.2-.2 2.3.6 1.4 1.8 2.7 3.1 3.3.8.3 1.4.1 1.7-.3l-1.1-1.1-.8.5c-.7-.4-1.3-1-1.7-1.7l.5-.8z" fill="#fff"/></svg>800.555.0142</li>
      <li><svg viewBox="0 0 10 10"><rect x="2.5" y="0.5" width="5" height="3"/><rect x="0" y="3.5" width="10" height="4" rx="1"/><rect x="2.5" y="6.5" width="5" height="3"/></svg>800.555.0199</li>
      <li><svg viewBox="0 0 10 10"><rect x="0" y="2" width="10" height="6.5"/><path d="M0.5 2.5 5 6 9.5 2.5" stroke="#fff" fill="none"/></svg>hello@meridelgroup.net</li>
    </ul>
    <div class="rule"></div>
    <p class="web">www.meridelgroup.net</p>
  </section>

</div>
</body>
</html>
```